Stickers signage for the outside of a 24 foot box truck.

This truck is for an oil field service truck, I have included a picture of the truck and the logo. The service is steam, heating and pressure washing for the oil field. Because of the large area to use for branding and advertising, I would like to have large decals placed on the truck, but not a full wrap due to the cost and the style is not what we are looking for.

I would like a series of large decals with log, phone number, email and some of the words mentioned, steam, heating, pressure washing place on. I would like some creativity in using the logo and graphics that compliment the logo. We are looking for edgy, and simplistic at the same time. Many truck wraps have so many things going on, the brand is lost. I have posted as well as example of a brand well recognized in the industry. Though I am not personally a fan of the truck design, it is well recognized instantly, and repeatable on each truck.

Given the name of the company Falcon Ridge, this gives the designer some leeway in using that in the design.

Sides, front, and back all available for signage.

Please only submit one design, unless the designs are completely different. I am looking for unique designs from different designers, and on one task done here, there were numerous similar designs submitted. Thank you for your submissions, all your hard work is appreciated.

There is a company called Teal Oilfield Services, they have a brand, recognizable and memorable. Very well designed. Also the task is now guaranteed.

0192cc
000000
ffffff

```html
<!DOCTYPE html>
<html lang="en">
<head>
<meta charset="utf-8">
<title>Falcon Ridge Oilfield Services Limited – Truck Decal</title>
<link rel="stylesheet" href="https://fonts.googleapis.com/css2?family=Audiowide&family=Orbitron:wght@700;900&display=swap">
<style>
  :root {
    --brand-blue: #2ea6da;
    --ink: #1c1c1c;
    --paper: #ffffff;
    --text-dark: #141414;
  }
  * { margin: 0; padding: 0; box-sizing: border-box; }
  html, body { width: 1200px; height: 723px; overflow: hidden; background: var(--paper); }
  .decal { position: relative; width: 1200px; height: 723px; background: var(--paper); }

  .header-band {
    position: absolute; left: 57px; top: 30px; width: 1086px; height: 202px;
    background: var(--ink); border-top-right-radius: 62px;
  }
  .brand-mark {
    position: absolute; left: 55px; top: 15px; width: 180px; height: 172px;
    background: var(--paper);
  }
  .brand-name {
    position: absolute; left: 262px; top: 22px; width: 800px;
    font-family: "Orbitron", sans-serif; font-weight: 900; font-size: 84px;
    line-height: 1; color: var(--paper); text-transform: uppercase; letter-spacing: 1px;
    white-space: nowrap;
  }
  .brand-tagline {
    position: absolute; left: 266px; top: 132px; width: 790px;
    font-family: "Orbitron", sans-serif; font-weight: 700; font-size: 29px;
    line-height: 1; color: var(--brand-blue); text-transform: uppercase;
    letter-spacing: 9px; white-space: nowrap;
  }

  .service {
    position: absolute; left: 57px; width: 690px; height: 131px; background: var(--ink);
  }
  .service--wash { top: 252px; }
  .service--steam { top: 402px; }
  .service--heat { top: 558px; }
  .service-icon {
    position: absolute; left: 40px; top: 10px; width: 136px; height: 111px;
    background: linear-gradient(to bottom, var(--paper) 0 55%, var(--brand-blue) 55% 100%);
  }
  .service-title {
    position: absolute; left: 195px; top: 30px;
    font-family: "Audiowide", sans-serif; font-size: 38px; line-height: 1;
    color: var(--paper); text-transform: uppercase; white-space: nowrap;
  }
  .service-note {
    position: absolute; left: 197px; top: 78px;
    font-family: "Audiowide", sans-serif; font-size: 21px; line-height: 1;
    color: var(--brand-blue); text-transform: uppercase; white-space: nowrap;
  }

  .contact-panel {
    position: absolute; left: 770px; top: 252px; width: 373px; height: 438px;
    background: var(--brand-blue); border-bottom-right-radius: 68px;
    text-align: center; color: var(--text-dark); font-family: "Audiowide", sans-serif;
  }
  .contact-label { position: absolute; left: 0; width: 100%; font-size: 42px; line-height: 1; text-transform: uppercase; }
  .contact-value { position: absolute; left: 0; width: 100%; line-height: 1; white-space: nowrap; }
  .contact-label--tel { top: 58px; }
  .contact-value--tel { top: 106px; font-size: 32px; }
  .contact-label--email { top: 246px; font-size: 46px; }
  .contact-value--email { top: 300px; font-size: 19px; text-transform: uppercase; }
</style>
</head>
<body>
<main class="decal">
  <header class="header-band">
    <div class="brand-mark" aria-hidden="true"></div>
    <h1 class="brand-name">Falcon Ridge</h1>
    <p class="brand-tagline">Oilfield Services Limited</p>
  </header>

  <section class="service service--wash">
    <div class="service-icon" role="img" aria-label="Pressure washer wand icon"></div>
    <h2 class="service-title">Pressure Washing</h2>
    <p class="service-note">Deep Pressure Wash</p>
  </section>

  <section class="service service--steam">
    <div class="service-icon" role="img" aria-label="Steam cloud icon"></div>
    <h2 class="service-title">Steam</h2>
    <p class="service-note">Lift the Dirt</p>
  </section>

  <section class="service service--heat">
    <div class="service-icon" role="img" aria-label="Flame icon"></div>
    <h2 class="service-title">Heating</h2>
    <p class="service-note">Heat Clean</p>
  </section>

  <aside class="contact-panel">
    <p class="contact-label contact-label--tel">Tel:</p>
    <p class="contact-value contact-value--tel">1-555-204-7316</p>
    <p class="contact-label contact-label--email">Email:</p>
    <p class="contact-value contact-value--email">falconridge@example.com</p>
  </aside>
</main>
</body>
</html>
```